MARLOW BAY SPIRITHOUSE BOTTLE LABELS

Hello Designers,

I would like to see the bottles literally be labeled as an absolute stand out from any competitor, incorporating eye-catching copper colour label background colour which matches the colour of my two Copper Pot Stills.

Front Label will be black font on copper label
saying:-

Marlow Bay Spirithouse

A "mn♢" water mark to be incorporated on main label (example attached)

Plus an outline of Marlow Bay, (located in Tasmania, Australia), suttle and cleverly included, but only to those who are particularly observant.

I also have visualised Angel wings in a copper outline with diamond details (photo of my necklace attached), incorporated with the two 55L copper stills (photo attached).

I have taken a photo of the Bronze Swallow Stills (as attached file ‘outline') and have done my best to edit it to show that I would just like the outline to be shown for the copper coloured label (no hoses or shadows should be in it).

Naturally, there are other labels needed to compliment the main Label on the bottle of spirit. For reference much of the rest of the standard information will be very similar to labels on other bottles in any bottle shop.

The Marlow Bay Spirithouse label separate to the Main Brand logo will be a different colour background & font

a Front) Gin Spirit Label)) - Blue colour font
Title = Marlow Bay Native Gin
_______ ml - Crafted to enjoy now
%Alc Vol _______ Standard Drinks ________

b Front Label) Vodka Spirit Label )) - Ruby colour font
Title = Marlow Bay Ruby Vodka
Crafted to enjoy now
____ ml ____%Alc Vol ____ Standard Drinks

c Front label) Whisky Single Malt Spirit Label )) - Green colour font
Title = Q42 Single Malt Whisky
Crafted and aged ready to enjoy now
Bottle # _______ Cask # & Type __________

a + b back Label) Information Label (for Gin & Vodka Bottles))

Spirit distilled by Nora Pellagrue in Bronze Swallow Stills
Bottled at Marlow Bay Spirithouse
Currie, Marlow Bay, Tasmania
Product of Australia (maybe use logo instead of text)
You'll find more Marlow Bay made Product and Gifts at
www.marlowbayspirits.example
Mobile: 0461 TOASTS

c Back label) Whisky Single Malt Spirit Label
Distilled at: Ferncliff Stillworks
Western Junction, Tasmania
Bottled by Nora Pellagrue
Marlow Bay Spirithouse
Product of Australia
Mobile: 0461 TOASTS

e Back label) Information label for all bottles and spirits
Recycle logo (Australian Standard)
Don't Drink While Pregnant Logo in Colour (details attached)
Blank white Angel Wings Shape shape Section (section for me to personally dedicate bottle by hand written signature)

3rd Section) mn✦ short & sweet story (yet to be finalised out of some of the info given below)

A bit more elaboration about this Project: My story is that I was made on Marlow Bay and I love living a life of freedom, walking daily on our bare beaches and taking photos of this amazing unique place and always able to find a smiling and supportive face. I am very passionate about our Island, all that is has to offer including our world class quality produce, the outstanding quality brand that we are well known for by everyone and the friendly locals.

A native Lady is very exciting to be running the 1st Distillery at 40 degrees South. Making Spirits on Marlow Bay in Bass Strait Tasmania, well known as the Roaring 40's. It is known to have the freshest / purest air in the world and likewise with rain water, it sure seems that was to us anyway. Also famous for the tallest lighthouse in the Southern Hemisphere built because of the large number of shipwrecks around Marlow Bay, especially the Pelorind.

My mission is to contribute more to our local economy and community and do this Island and our Industry proud, by way of building and operating a profitable first class boutique spirit distillery that can grow with demand. Using our local products and botanicals to make our very own beautiful beverages to be enjoyed by my Family, residents, visitors and those from afar.

After 7 years in design, now distilling with 2 custom made Copper 55L Pot Stills, namely my Still Swallows, that travelled across wild seas on a Cray Boat to their new home and are now making award winning spirits.
Namely Gin, using Marlow Bay coastal and beachside botanicals, also Ruby Grapefruit & Ginger Vodka. In addition I will also be releasing Q42 Single Malt Whisky.

To follow will be other varieties made with Local Produce such as Marlow Bay apple and Marlow Bay honey spirits and this range will grow with demand.

The growing Industry as I know it, the Distillers and their Teams are fun, friendly with passion and professionalism about awesome alcoholic beverages.

Marlow Bay Spirithouse Sales will be aimed predominantly people visiting the Island. Our market is predominately Golfers, as Marlow Bay has two very highly ranked Public Links Courses in Australia and the World. Websites and Podcast still to be developed will which build relationships with current and new people, share our entertaining distilling journey and provide educational information about our Industry and surrounds that make our product such great quality with the naturally amazing wild yeasts and so on.

Marlow Bay Spirithouse will also be selling bottles online and posting orders from Marlow Bay to Australia, whereby we want our final design be a simple, effective and consistent brand that shines of natural outstanding qualities of our spirits. Creating an exciting and unforgettable unboxing experience to keep our customers coming back to buy more bottles of spirits from Marlow Bay Spirithouse.

The logo chosen will set us apart from the rest making Marlow Bay Spirithouse easily recognisable and people will respond with a smile and buy bottles. They will be compelled to proudly share the news of their purchase and details of the Distillery far and wide on a variety of Media platforms and consistently returning for more of our delicious Products.

Bottles of Spirit made by Marlow Bay Spirithouse will also be the new gift to give both males and females, plus a great present to give to those celebrating any occasion.
Customers will be given the opportunity for the bottle to be dedicated as a one of a kind for themselves of as a gift, hand-signed with a personalised note to the person from Merry Nora | Marlow Bay Spirithouse.

Furthermore a series of unique hand made small batch collectables will be next in design…..

Bottles details at this stage are…. (but subject to change)

200ML & 700ML OSLO STYLE BOTTLES MARCH 2020 BOTTLES AT MB SPIRITHOUSE
http://www.vitrepack.example/b7742kq.html

700ml size are to be served behind bars and in restaurants
200ml make the perfect gift and travel size.
Will also be selling 200ml in gift packs of 3 in a black Jute bag with cane handles and a see through face.
Thank you so much, happy to discuss further to help with design finalisation.
mn✦
NORA
Updates

Hello, My Sincere apologies that I have not responded sooner. Thank you all for your patience.

Target Market(s)

Golfers, award winning hand-made Spirit appreciators and collectors

Font styles to use
Other font styles liked:
• Sweetly Drawn has been used previously for the mn✦

Requirements
Must have
• Stand out
Copper Background on Main Label
Nice to have
• Please see in Project description what I think would be nice. Also attached files help to visualise what I have in mind.
Should not have
• I wouldn't tell a great designer what not to do :-)

```html
<!DOCTYPE html>
<html lang="en">
<head>
<meta charset="UTF-8">
<title>Marlow Bay Ruby Vodka – Front Label</title>
<link href="https://fonts.googleapis.com/css2?family=Lobster+Two:ital,wght@1,400;1,700&family=Work+Sans:wght@400;500&display=swap" rel="stylesheet">
<style>
  :root {
    --backdrop: #b9bcc1;
    --ruby: #9b1c2b;
    --ribbon: #c64a57;
    --copper-light: #efdccd;
    --copper-mid: #e2c8b6;
    --copper-dark: #d6b8a4;
    --cream: #fff6ef;
  }
  html, body {
    margin: 0;
    padding: 0;
    width: 960px;
    height: 1200px;
    overflow: hidden;
    background: var(--backdrop);
  }
  .canvas {
    position: relative;
    width: 960px;
    height: 1200px;
  }
  .label {
    position: absolute;
    left: 60px;
    top: 285px;
    width: 840px;
    height: 630px;
    background:
      repeating-linear-gradient(90deg, rgba(255,255,255,0.06) 0 2px, rgba(0,0,0,0.02) 2px 5px),
      linear-gradient(100deg, var(--copper-dark) 0%, var(--copper-light) 40%, var(--copper-mid) 75%, var(--copper-dark) 100%);
    font-family: "Work Sans", Arial, sans-serif;
    color: var(--ruby);
  }
  .band {
    position: absolute;
    left: 0;
    width: 100%;
    height: 10px;
    background: var(--ruby);
  }
  .band::after {
    content: "";
    position: absolute;
    left: 0;
    width: 100%;
    height: 3px;
    background: var(--ruby);
  }
  .band--top { top: 0; }
  .band--top::after { top: 16px; }
  .band--bottom { bottom: 0; }
  .band--bottom::after { bottom: 16px; }
  .island-outline {
    position: absolute;
    left: 395px;
    top: 82px;
    width: 50px;
    height: 84px;
    background: var(--ruby);
    border-radius: 40% 30% 45% 35% / 20% 30% 40% 45%;
  }
  .product-title {
    position: absolute;
    left: 0;
    top: 172px;
    width: 100%;
    margin: 0;
    text-align: center;
    font-family: "Lobster Two", "Brush Script MT", cursive;
    font-style: italic;
    font-weight: 700;
    font-size: 104px;
    line-height: 1;
    color: var(--ruby);
  }
  .product-type {
    position: absolute;
    left: 0;
    top: 298px;
    width: 100%;
    margin: 0;
    text-align: center;
    font-weight: 500;
    font-size: 46px;
    letter-spacing: 6px;
    color: var(--ruby);
  }
  .tagline-ribbon {
    position: absolute;
    left: 200px;
    top: 385px;
    width: 440px;
    height: 90px;
  }
  .tagline-ribbon svg { position: absolute; inset: 0; }
  .tagline {
    position: absolute;
    inset: 0;
    margin: 0;
    display: flex;
    align-items: center;
    justify-content: center;
    font-family: "Lobster Two", "Brush Script MT", cursive;
    font-style: italic;
    font-size: 32px;
    color: var(--cream);
    transform: rotate(-5deg);
  }
  .details {
    position: absolute;
    left: 0;
    bottom: 34px;
    width: 100%;
    height: 70px;
  }
  .abv {
    position: absolute;
    left: 18px;
    bottom: 12px;
    font-size: 18px;
  }
  .volume {
    position: absolute;
    left: 0;
    width: 100%;
    bottom: 6px;
    text-align: center;
    font-size: 38px;
    letter-spacing: 1px;
  }
  .origin {
    position: absolute;
    right: 22px;
    bottom: 12px;
    font-size: 18px;
    line-height: 1.35;
    text-align: left;
  }
</style>
</head>
<body>
  <main class="canvas">
    <section class="label">
      <div class="band band--top"></div>

      <div class="island-outline" role="img" aria-label="Small outline map of the home island"></div>

      <h1 class="product-title">Marlow Bay</h1>
      <h2 class="product-type">RUBY VODKA</h2>

      <div class="tagline-ribbon">
        <svg viewBox="0 0 440 90" width="440" height="90" aria-hidden="true">
          <path d="M10 52 L420 14 L404 36 L430 56 L20 94 L36 72 Z" fill="var(--ribbon)" transform="translate(0,-8)"/>
        </svg>
        <p class="tagline">Crafted to enjoy now</p>
      </div>

      <div class="details">
        <span class="abv">40% Alc</span>
        <span class="volume">350ml</span>
        <span class="origin">Made in<br>Tasmania, Australia</span>
      </div>

      <div class="band band--bottom"></div>
    </section>
  </main>
</body>
</html>
```